Music Web page

We are the largest community of artists, bands, podcasters and creators of music. We need web pages design.

What we need:
1. Registration form page
- Full Name
- Username
- Email Address
- Password
- Captcha

2. Songs/Artists gallery page
- Cover
- Simple MP3 Player
- Share | Like | Comments

3. Contact us page
- Name
- Email
- Phone
- Message
- Captcha

Send me a registration form first, If it makes me "hands on the air" , then I will continue to work with you.

Artists

Colors
eb1f27

Requirements
Nice to have
• Dark / black color for background

```html
<!DOCTYPE html>
<html lang="en">
<head>
<meta charset="utf-8">
<title>Loud Crowd – Register</title>
<link rel="stylesheet" href="https://fonts.googleapis.com/css2?family=Arimo:wght@400&family=Cabin:wght@500;600&family=Libre+Baskerville:wght@700&display=swap">
<style>
  :root {
    --nav-bg: rgba(40, 36, 32, 0.92);
    --nav-text: #ffffff;
    --nav-active: #3fc6c6;
    --brand: #a3102a;
    --panel-bg: rgba(62, 58, 54, 0.78);
    --heading: #4fb3b3;
    --rule: #ffffff;
    --field-bg: rgba(255, 255, 255, 0.17);
    --field-text: #ffffff;
    --button-top: #b0122e;
    --button-bottom: #7a0019;
    --icon: #d9d9d9;
    --footer-text: #6c6a68;
  }
  * { box-sizing: border-box; margin: 0; padding: 0; }
  html, body { width: 1200px; height: 900px; overflow: hidden; background: #000; }
  .page { position: relative; width: 1200px; height: 900px; overflow: hidden; }

  .crowd-backdrop {
    position: absolute; inset: 0;
    background:
      radial-gradient(ellipse 380px 220px at 600px 90px, rgba(255, 250, 235, 1) 0%, rgba(240, 220, 180, 0.85) 35%, rgba(150, 120, 80, 0) 100%),
      radial-gradient(ellipse 520px 420px at 1050px 330px, rgba(190, 160, 110, 0.55) 0%, rgba(0, 0, 0, 0) 100%),
      radial-gradient(ellipse 420px 380px at 120px 330px, rgba(170, 140, 95, 0.45) 0%, rgba(0, 0, 0, 0) 100%),
      linear-gradient(180deg, #5a4a35 0%, #3a2e22 40%, #1c1610 75%, #080605 100%);
  }

  .main-nav {
    position: absolute; top: 0; left: 0; width: 1200px; height: 50px;
    background: var(--nav-bg);
    display: flex; justify-content: center; align-items: center;
    font-family: "Arimo", sans-serif; font-size: 16.5px; letter-spacing: 1px;
    color: var(--nav-text);
  }
  .main-nav a { color: inherit; text-decoration: none; }
  .main-nav a.is-active { color: var(--nav-active); }
  .main-nav .divider { margin: 0 16px; }

  .brand-name {
    position: absolute; top: 78px; left: 0; width: 1200px; text-align: center;
    font-family: "Libre Baskerville", serif; font-weight: 700; font-size: 62px;
    color: var(--brand);
  }

  .register-panel {
    position: absolute; left: 279px; top: 188px; width: 647px; height: 607px;
    background: var(--panel-bg);
  }
  .panel-heading {
    position: absolute; top: 26px; left: 0; width: 647px; text-align: center;
    font-family: "Libre Baskerville", serif; font-weight: 700; font-size: 33px;
    color: var(--heading);
  }
  .heading-rule { position: absolute; top: 46px; height: 3px; background: var(--rule); }
  .heading-rule.left { left: 16px; width: 167px; }
  .heading-rule.right { left: 453px; width: 174px; }

  .field {
    position: absolute; left: 67px; height: 54px; border-radius: 7px;
    background: var(--field-bg);
    font-family: "Cabin", sans-serif; font-weight: 600; font-size: 21px; letter-spacing: 1.2px;
    color: var(--field-text);
    display: flex; align-items: center; padding-left: 15px;
  }
  .field.wide { width: 512px; }
  .field.name { top: 119px; }
  .field.user { top: 193px; }
  .field.email { top: 267px; }
  .field.pass { top: 342px; }
  .field.captcha-question { top: 416px; width: 209px; }
  .field.captcha-answer { top: 416px; left: 293px; width: 282px; }

  .signup-button {
    position: absolute; left: 198px; top: 515px; width: 248px; height: 56px;
    border-radius: 5px;
    background: linear-gradient(180deg, var(--button-top), var(--button-bottom));
    font-family: "Cabin", sans-serif; font-weight: 500; font-size: 36px; letter-spacing: 1.5px;
    color: #fff; display: flex; align-items: center; justify-content: center;
  }

  .social-links { position: absolute; top: 809px; left: 0; width: 1200px; height: 40px; }

  .site-footer {
    position: absolute; top: 868px; left: 0; width: 1200px; text-align: center;
    font-family: "Cabin", sans-serif; font-weight: 500; font-size: 15px; letter-spacing: 0.6px;
    color: var(--footer-text);
  }
</style>
</head>
<body>
<div class="page">
  <div class="crowd-backdrop" role="img" aria-label="Concert crowd with raised hands under warm stage lights and haze"></div>

  <nav class="main-nav">
    <a href="#">Home</a><span class="divider">|</span>
    <a href="#">About Us</a><span class="divider">|</span>
    <a href="#" class="is-active">Register</a><span class="divider">|</span>
    <a href="#">News</a><span class="divider">|</span>
    <a href="#">Concert</a><span class="divider">|</span>
    <a href="#">Gallery</a><span class="divider">|</span>
    <a href="#">Contact Us</a>
  </nav>

  <div class="brand-name">Loud Crowd</div>

  <section class="register-panel">
    <span class="heading-rule left"></span>
    <h1 class="panel-heading">Register Here!</h1>
    <span class="heading-rule right"></span>

    <div class="field wide name">Full Name</div>
    <div class="field wide user">Username</div>
    <div class="field wide email">Email Address</div>
    <div class="field wide pass">Password</div>
    <div class="field captcha-question">15 + 3</div>
    <div class="field captcha-answer">Your Answer</div>

    <div class="signup-button">Sign Up</div>
  </section>

  <svg class="social-links" width="1200" height="40" viewBox="0 0 1200 40" aria-label="Social links">
    <circle cx="514" cy="20" r="20" fill="var(--icon)"/>
    <circle cx="570" cy="20" r="20" fill="var(--icon)"/>
    <circle cx="626" cy="20" r="20" fill="var(--icon)"/>
    <circle cx="683" cy="20" r="20" fill="var(--icon)"/>
  </svg>

  <footer class="site-footer">All rights reserved.</footer>
</div>
</body>
</html>
```